Thorne Consulting, Business Cards for International Development Consultancy

I'm an independent consultant working in the international development sector. I work with small organisations in developing countries to help them develop their community based programs so that they can be internationally competitive. This means they need to work better with their own communities to deliver meaningful quality work and also improve the accountability of their work so that they can compete for international and domestic funding.

I like the idea of being a connector between community, local organisations and international best practice and back again (ie acknowledging that international best practice can learn a lot from community).

My surname is Thorne - so I'd like the logo to use the idea of web as a connector.

I work with people with sight impairments - would like my card to be useful for low vision (i.e. clear graphics, easy to read font) and no vision (i.e. brail).

Target Market(s)

international non-government organisations (i.e. harvestaid, bright futures trust, open horizons), Blue Anchor Relief Alliance, government (i.e. Australian Bureau of Overseas Partnerships, consulars), non government agencies,

Industry/Entity Type

Business

Contact Information for Business Card

International Development Consultant
Connecting International Development with Community

Kerry Thorne
Lead Consultant
Phone: +61 417 382519
Email: kthorne.consulting@mailvale.com

Font styles to use
Sans Serif

Colors
eaf1f7
85acd3
d3a5cc
0456a4
a64599
0255a3

Requirements
Nice to have
• brail
Should not have
• fancy fonts - needs to be easy to read.

```html
<!DOCTYPE html>
<html lang="en">
<head>
<meta charset="utf-8">
<title>Thorne Consulting – Business Cards</title>
<link rel="stylesheet" href="https://fonts.googleapis.com/css2?family=Questrial&family=Open+Sans:wght@400;600;700&display=swap">
<style>
  :root {
    --blue-deep: #0456a4;
    --blue-dark: #0255a3;
    --blue-soft: #85acd3;
    --blue-mist: #eaf1f7;
    --ink: #2b2f36;
    --ink-muted: #5a5f66;
    --paper: #ffffff;
    --stage: #e4e9ef;
  }
  * { margin: 0; padding: 0; box-sizing: border-box; }
  html, body {
    width: 1200px;
    height: 900px;
    overflow: hidden;
    background: var(--stage);
  }
  .canvas {
    position: relative;
    width: 1200px;
    height: 900px;
  }
  .card {
    position: absolute;
    left: 250px;
    width: 700px;
    height: 400px;
    border-radius: 4px;
    overflow: hidden;
    box-shadow: 0 6px 18px rgba(20, 40, 70, 0.18);
  }

  /* Front */
  .card-front {
    top: 35px;
    background: linear-gradient(160deg, #1565b2 0%, var(--blue-deep) 55%, var(--blue-dark) 100%);
  }
  .front-lockup {
    position: absolute;
    left: 0; right: 0;
    top: 118px;
    text-align: center;
  }
  .brand-dot {
    display: block;
    margin: 0 auto 14px;
    width: 46px;
    height: 46px;
    border-radius: 50%;
  }
  .card-front .brand-dot { background: var(--paper); }
  .brand-name {
    font-family: "Questrial", sans-serif;
    font-weight: 400;
    font-size: 44px;
    line-height: 1;
    letter-spacing: 0.5px;
  }
  .card-front .brand-name { color: var(--paper); }
  .brand-tagline {
    font-family: "Open Sans", sans-serif;
    font-size: 17px;
    margin-top: 8px;
    letter-spacing: 0.2px;
  }
  .card-front .brand-tagline { color: var(--blue-soft); }

  /* Back */
  .card-back {
    top: 465px;
    background: var(--paper);
  }
  .back-lockup {
    position: absolute;
    left: 0; right: 0;
    top: 46px;
    text-align: center;
  }
  .card-back .brand-dot { background: var(--blue-deep); }
  .card-back .brand-name { color: var(--blue-deep); }
  .card-back .brand-tagline { color: var(--blue-soft); }

  .person {
    position: absolute;
    left: 160px;
    top: 218px;
    width: 160px;
    text-align: right;
    font-family: "Open Sans", sans-serif;
  }
  .person-name {
    font-weight: 700;
    font-size: 19px;
    color: var(--blue-deep);
  }
  .person-role {
    font-size: 18px;
    color: var(--ink-muted);
    margin-top: 2px;
  }
  .divider {
    position: absolute;
    left: 348px;
    top: 216px;
    width: 1px;
    height: 80px;
    background: linear-gradient(to bottom, transparent, #b9c6d4 25%, #b9c6d4 75%, transparent);
  }
  .contacts {
    position: absolute;
    left: 372px;
    top: 214px;
    list-style: none;
    font-family: "Open Sans", sans-serif;
    font-size: 17px;
    color: var(--ink);
  }
  .contacts li {
    display: flex;
    align-items: center;
    height: 30px;
  }
  .contact-icon {
    width: 18px;
    height: 18px;
    margin-right: 12px;
    flex: none;
    color: var(--blue-deep);
  }
  .contact-at {
    font-weight: 700;
    font-size: 17px;
    text-align: center;
    line-height: 18px;
  }
  .base-band {
    position: absolute;
    left: 0; right: 0; bottom: 0;
    height: 56px;
    background: linear-gradient(90deg, var(--blue-dark), #1565b2);
  }
</style>
</head>
<body>
<main class="canvas">

  <section class="card card-front" aria-label="Business card front">
    <div class="front-lockup">
      <span class="brand-dot"></span>
      <p class="brand-name">Thorne Consulting</p>
      <p class="brand-tagline">International Development Consultancy</p>
    </div>
  </section>

  <section class="card card-back" aria-label="Business card back">
    <div class="back-lockup">
      <span class="brand-dot"></span>
      <p class="brand-name">Thorne Consulting</p>
      <p class="brand-tagline">International Development Consultancy</p>
    </div>

    <div class="person">
      <p class="person-name">Dalen Pryce</p>
      <p class="person-role">Manager</p>
    </div>

    <div class="divider"></div>

    <ul class="contacts">
      <li>
        <svg class="contact-icon" viewBox="0 0 24 24" aria-hidden="true">
          <path fill="currentColor" d="M6.6 10.8a15.1 15.1 0 0 0 6.6 6.6l2.2-2.2a1 1 0 0 1 1-.25 11.4 11.4 0 0 0 3.6.57 1 1 0 0 1 1 1V20a1 1 0 0 1-1 1A17 17 0 0 1 3 4a1 1 0 0 1 1-1h3.5a1 1 0 0 1 1 1c0 1.25.2 2.45.57 3.6a1 1 0 0 1-.25 1z"/>
        </svg>
        <span>555 018 2746</span>
      </li>
      <li>
        <svg class="contact-icon" viewBox="0 0 24 24" aria-hidden="true">
          <g fill="none" stroke="currentColor" stroke-width="1.8">
            <circle cx="12" cy="12" r="9"/>
            <ellipse cx="12" cy="12" rx="4" ry="9"/>
            <line x1="3" y1="12" x2="21" y2="12"/>
            <path d="M5 7h14M5 17h14"/>
          </g>
        </svg>
        <span>www.dalenpryce.net</span>
      </li>
      <li>
        <span class="contact-icon contact-at" aria-hidden="true">@</span>
        <span>dpryce@inboxvale.com</span>
      </li>
    </ul>

    <div class="base-band"></div>
  </section>

</main>
</body>
</html>
```